Delivery Performance Dashboard for Web Portal

We need you to design a dashboard for our web portal. We deliver sand and stone to construction jobsites. The attached screenshot is from our current web portal dashboard . It shows how much material has been delivered from an order.

Haulwell will deliver multiple loads during the day and the dispatcher uses the dashboard to monitor if they need to add more trucks or less trucks to fulfill the order. An example would be, I need to ship 1,000 tons of sand to a jobsite and I plan to use 10 trucks during the day and that it will take 10 hours of hauling to complete the job. After 5 hours of hauling (50% the day is over), I should have delivered 500 tons of sand (50% of the order). But maybe there is a lot of traffic, and I only have delivered 300 tons. The dashboard will show that I am behind schedule and I might need to add 2 more trucks to the job.

Industry/Entity Type

Construction

Font styles to use
Sans Serif

Requirements
Must have
• We need a progress bar showing how much material has been delivered, how much material was requested to be delivered total and how much material should have been delivered at the current time. The goal is to show the user if the deliveries are ahead or behind the expected pace and why.
Nice to have
• The icons for plant, driving and jobsite show if the actual times have exceeded or beaten the planned times. Maybe you have other ideas to show the user if the trucks are sitting longer on the jobsite, at the plant to get loaded or driving to and from the jobsite.

```html
<!DOCTYPE html>
<html lang="en">
<head>
<meta charset="utf-8">
<title>Haulwell – Delivery Dashboard</title>
<link href="https://fonts.googleapis.com/css2?family=IBM+Plex+Sans:wght@400;500;600;700&display=swap" rel="stylesheet">
<style>
:root{
  --stage:#484848;
  --teal:#00a48a;
  --teal-dark:#008f78;
  --orange:#f37021;
  --ink:#2c2c2c;
  --head:#333333;
  --page:#f5f4f4;
  --row-alt:#f0efef;
  --track:#e3e3e3;
  --red:#e53935;
  --green:#19a98c;
  --muted:#9a9a9a;
}
*{box-sizing:border-box;margin:0;padding:0}
html,body{width:1200px;height:1099px;overflow:hidden}
body{background:var(--stage);font-family:"IBM Plex Sans",Arial,sans-serif;color:var(--ink);position:relative}
.frame{position:absolute;width:1025px;height:447px;background:var(--page);overflow:hidden}
.frame-top{left:90px;top:73px}
.frame-bottom{left:88px;top:565px}
.sidebar{position:absolute;left:0;top:0;width:118px;height:100%;background:var(--teal)}
.brand{height:76px;display:flex;align-items:center;padding-left:10px;color:#fff;font-weight:600;font-size:13px;letter-spacing:.3px}
.nav{list-style:none}
.nav li{height:35px;display:flex;align-items:center;padding-left:8px;color:#fff;font-weight:600;font-size:9.5px;letter-spacing:.3px;border-bottom:1px solid var(--teal-dark)}
.nav li svg{width:13px;height:13px;margin-right:9px;flex:none}
.nav li.active{background:#fff;color:var(--orange);border-left:2px solid var(--orange);padding-left:6px}
.topbar{position:absolute;left:118px;top:0;right:0;height:33px;background:#fff;box-shadow:0 1px 2px rgba(0,0,0,.05)}
.user{position:absolute;right:22px;top:8px;display:flex;align-items:center;font-size:6.5px;font-weight:600;line-height:8.5px}
.avatar{width:17px;height:17px;border-radius:50%;border:1.5px solid var(--teal);background:#c9b9a8;margin-right:6px}
.user .chev{margin-left:10px;width:7px;height:7px}
.orders{position:absolute;left:134px;top:76px;width:875px;border-collapse:collapse;table-layout:fixed;background:#fff;box-shadow:0 1px 3px rgba(0,0,0,.06)}
.orders th{background:var(--head);color:#fff;font-size:6.5px;font-weight:600;text-align:left;height:23px;padding-left:13px;border-right:1px solid #4a4a4a;letter-spacing:.2px}
.orders th.center{text-align:center;padding-left:0}
.orders th .hd-truck{width:9px;height:7px;vertical-align:-1px;margin-left:3px}
.orders td{height:35px;font-size:8.5px;padding-left:13px;vertical-align:top;padding-top:16px;border-right:1px solid #ececec;white-space:nowrap}
.orders tbody tr:nth-child(even){background:var(--row-alt)}
.orders td.tons{padding-top:19px;padding-left:13px}
.bar{width:146px;height:4px;background:var(--track);border-radius:2px;overflow:hidden}
.bar i{display:block;height:100%;background:var(--teal);border-radius:2px}
.tons-meta{display:flex;justify-content:space-between;width:146px;font-size:6px;margin-top:4px}
.wait{padding-top:19px!important;padding-left:12px!important}
.wait svg{width:52px;height:8px;display:block}
.rem,.diff{font-size:7px!important;padding-top:17px!important}
.diff{text-align:center;padding-left:0!important}
.up{color:var(--green)}
.down{color:var(--red)}
.pager{position:absolute;right:20px;top:335px;display:flex;align-items:center;font-size:8px}
.pager span{width:18px;text-align:center}
.pager .on{width:11px;height:11px;border-radius:50%;background:var(--orange);color:#fff;line-height:11px;font-size:7px;margin:0 3.5px}
.pager .arrow{color:var(--muted)}
.copyright{position:absolute;left:118px;right:0;top:420px;text-align:center;font-size:7.5px}
.code{position:absolute;right:6px;top:431px;font-size:7.5px}
.cycle{position:absolute;left:801px;top:138px;width:151px;height:164px;background:#fff;box-shadow:0 2px 8px rgba(0,0,0,.18);padding:9px 10px;font-size:6.5px;color:var(--ink)}
.cycle::before{content:"";position:absolute;left:62px;top:-4px;width:8px;height:8px;background:#fff;transform:rotate(45deg)}
.cycle-title{padding-bottom:6px;border-bottom:1px solid #dcdcdc;margin-bottom:6px}
.leg{display:flex;align-items:center;height:31px;border-bottom:1px solid #e6e6e6}
.leg:last-child{border-bottom:0}
.leg-icon{width:17px;height:17px;border-radius:50%;background:var(--teal);margin-right:6px;flex:none;display:flex;align-items:center;justify-content:center}
.leg-icon svg{width:9px;height:9px}
.leg-body{flex:1;line-height:9px}
.leg-name{font-weight:500;color:var(--ink)}
.leg-row{display:flex;justify-content:space-between}
</style>
</head>
<body>

<svg width="0" height="0" style="position:absolute">
  <defs>
    <symbol id="ico-wait" viewBox="0 0 52 8">
      <g fill="#8a8a8a">
        <path d="M0 8V3l2 1V2l2 2V2l2 2V1h1v7z"/>
        <path d="M20 1h5v5h-5zM25 3h2l1.5 2v1H25z"/>
        <circle cx="21.5" cy="6.8" r="1.1"/><circle cx="26.5" cy="6.8" r="1.1"/>
        <path d="M41 0a2.5 2.5 0 0 1 2.5 2.5C43.5 4.5 41 8 41 8s-2.5-3.5-2.5-5.5A2.5 2.5 0 0 1 41 0zm0 1.5a1 1 0 1 0 0 2 1 1 0 0 0 0-2z"/>
      </g>
      <path d="M9 5.5l1.5-2 1.5 2z" fill="#e53935"/>
      <path d="M30 5.5l1.5-2 1.5 2z" fill="#e53935"/>
      <path d="M45 4l1.5 2 1.5-2z" fill="#19a98c"/>
    </symbol>
    <symbol id="ico-plant" viewBox="0 0 10 10"><path d="M0 10V4l3 2V4l3 2V4l2 1V0h2v10z" fill="#fff"/></symbol>
    <symbol id="ico-truck" viewBox="0 0 10 10"><path d="M0 2h6v5H0zM6 4h2.5L10 6v1H6z" fill="#fff"/><circle cx="2" cy="8" r="1.3" fill="#fff"/><circle cx="8" cy="8" r="1.3" fill="#fff"/></symbol>
    <symbol id="ico-truck-grey" viewBox="0 0 10 10"><path d="M0 2h6v5H0zM6 4h2.5L10 6v1H6z" fill="#9a9a9a"/><circle cx="2" cy="8" r="1.3" fill="#9a9a9a"/><circle cx="8" cy="8" r="1.3" fill="#9a9a9a"/></symbol>
    <symbol id="ico-pin" viewBox="0 0 10 10"><path d="M5 0a3.5 3.5 0 0 1 3.5 3.5C8.5 6 5 10 5 10S1.5 6 1.5 3.5A3.5 3.5 0 0 1 5 0zm0 2a1.4 1.4 0 1 0 0 2.8A1.4 1.4 0 0 0 5 2z" fill="#fff"/></symbol>
    <symbol id="ico-gear" viewBox="0 0 10 10"><circle cx="5" cy="5" r="3.3" fill="none" stroke="#fff" stroke-width="1.8" stroke-dasharray="1.6 1"/><circle cx="5" cy="5" r="1.2" fill="#fff"/></symbol>
  </defs>
</svg>

<!-- Dashboard: default state -->
<section class="frame frame-top">
  <aside class="sidebar">
    <div class="brand">HAULWELL</div>
    <ul class="nav">
      <li class="active"><svg viewBox="0 0 14 14" fill="none" stroke="currentColor" stroke-width="1.2"><path d="M2 7l5-5 5 5M3.5 6v6h7V6"/><path d="M6 12V9h2v3"/></svg>DASHBOARD</li>
      <li><svg viewBox="0 0 14 14" fill="none" stroke="#fff" stroke-width="1.2"><circle cx="7" cy="4.5" r="3"/><path d="M1.5 13.5a5.5 5 0 0 1 11 0"/></svg>EMPLOYEES</li>
      <li><svg viewBox="0 0 14 14" fill="none" stroke="#fff" stroke-width="1.1"><rect x="1" y="2.5" width="11" height="10"/><path d="M1 5.5h11M4 1v3M9 1v3"/><circle cx="10.5" cy="10.5" r="2.3" fill="var(--teal)"/></svg>CALENDAR</li>
      <li><svg viewBox="0 0 14 14" fill="none" stroke="#fff" stroke-width="1.1"><circle cx="7" cy="7" r="6"/><circle cx="7" cy="7" r="3.8"/><circle cx="7" cy="7" r="1.6"/></svg>EXPENSES</li>
      <li><svg viewBox="0 0 14 14" fill="none" stroke="#fff" stroke-width="1.1"><path d="M1 13h12M2 13V9h2v4M6 13V7h2v6M10 13V5h2v8M2 6l4-3 3 2 4-4"/></svg>PERFORMANCE</li>
      <li><svg viewBox="0 0 14 14" fill="none" stroke="#fff" stroke-width="1.1"><rect x="2" y="1" width="8" height="12"/><path d="M4 4h4M4 6.5h4M4 9h4M10 5h2v8h-2"/></svg>REPORTS</li>
      <li><svg viewBox="0 0 10 10"><use href="#ico-gear"/></svg>SETTINGS</li>
      <li></li>
      <li></li>
    </ul>
  </aside>
  <header class="topbar">
    <div class="user"><span class="avatar" role="img" aria-label="User avatar"></span><span>ADMIN, DEMO<br>HR ADMINISTRATOR</span><svg class="chev" viewBox="0 0 8 8"><path d="M1 3l3 3 3-3" fill="none" stroke="#333" stroke-width="1"/></svg></div>
  </header>
  <table class="orders">
    <colgroup><col style="width:54px"><col style="width:111px"><col style="width:134px"><col style="width:170px"><col style="width:61px"><col style="width:174px"><col style="width:71px"><col style="width:60px"><col style="width:40px"></colgroup>
    <thead><tr><th>ORDER</th><th>ORIGIN</th><th>DESTINATION</th><th>CUSTOMER</th><th>STATUS</th><th class="center">TONS</th><th class="center">WAIT TIME</th><th class="center">REMAINING</th><th>+/-<svg class="hd-truck"><use href="#ico-truck-grey"/></svg></th></tr></thead>
    <tbody>
      <tr><td>17746</td><td>Marlow Asphalet Plant</td><td>KRTM - 185 from mm 77-98</td><td>Hollis Construction = North Division</td><td>Accepted</td><td class="tons"><div class="bar"><i style="width:53%"></i></div><div class="tons-meta"><span>722.57/1500</span><span>7.30am-5.00pm</span></div></td><td class="wait"><svg><use href="#ico-wait"/></svg></td><td class="rem up">+1.25 hrs</td><td class="diff down">-31</td></tr>
      <tr><td>17747</td><td>Carver Asphalet Plant</td><td>Maple Sprins</td><td>Hollis Construction = North Division</td><td>Accepted</td><td class="tons"><div class="bar"><i style="width:100%"></i></div><div class="tons-meta"><span>1830.79 / 1000</span><span>7.30am-5.00pm</span></div></td><td class="wait"><svg><use href="#ico-wait"/></svg></td><td class="rem down">-0.28 hrs</td><td class="diff up">+16</td></tr>
      <tr><td>17794</td><td>Marlow Asphalet Plant</td><td>KRTM - 185 from mm 77-98</td><td>Hollis Construction = North Division</td><td>Accepted</td><td class="tons"><div class="bar"></div><div class="tons-meta"><span>0.00 / 100</span><span>8.00pm - 4.00am</span></div></td><td class="wait"><svg><use href="#ico-wait"/></svg></td><td class="rem">8.00 hrs</td><td class="diff up">-</td></tr>
      <tr><td>17746</td><td>Marlow Asphalet Plant</td><td>KRTM - 185 from mm 77-98</td><td>Hollis Construction = North Division</td><td>Accepted</td><td class="tons"><div class="bar"><i style="width:53%"></i></div><div class="tons-meta"><span>722.57/1500</span><span>7.30am-5.00pm</span></div></td><td class="wait"><svg><use href="#ico-wait"/></svg></td><td class="rem up">+1.25 hrs</td><td class="diff down">-31</td></tr>
      <tr><td>17747</td><td>Carver Asphalet Plant</td><td>Maple Sprins</td><td>Hollis Construction = North Division</td><td>Accepted</td><td class="tons"><div class="bar"><i style="width:100%"></i></div><div class="tons-meta"><span>1830.79 / 1000</span><span>7.30am-5.00pm</span></div></td><td class="wait"><svg><use href="#ico-wait"/></svg></td><td class="rem down">-0.28 hrs</td><td class="diff up">+16</td></tr>
      <tr><td>17794</td><td>Marlow Asphalet Plant</td><td>KRTM - 185 from mm 77-98</td><td>Hollis Construction = North Division</td><td>Accepted</td><td class="tons"><div class="bar"></div><div class="tons-meta"><span>0.00 / 100</span><span>8.00pm - 4.00am</span></div></td><td class="wait"><svg><use href="#ico-wait"/></svg></td><td class="rem">8.00 hrs</td><td class="diff up">-</td></tr>
    </tbody>
  </table>
  <nav class="pager"><span class="arrow">‹</span><span class="on">1</span><span>2</span><span>3</span><span>4</span><span>5</span><span class="arrow">›</span></nav>
  <p class="copyright">Copyright © 2020 All Rights Reserved</p>
  <p class="code">X37</p>
</section>

<!-- Dashboard: cycle time breakdown open -->
<section class="frame frame-bottom">
  <aside class="sidebar">
    <div class="brand">HAULWELL</div>
    <ul class="nav">
      <li class="active"><svg viewBox="0 0 14 14" fill="none" stroke="currentColor" stroke-width="1.2"><path d="M2 7l5-5 5 5M3.5 6v6h7V6"/><path d="M6 12V9h2v3"/></svg>DASHBOARD</li>
      <li><svg viewBox="0 0 14 14" fill="none" stroke="#fff" stroke-width="1.2"><circle cx="7" cy="4.5" r="3"/><path d="M1.5 13.5a5.5 5 0 0 1 11 0"/></svg>EMPLOYEES</li>
      <li><svg viewBox="0 0 14 14" fill="none" stroke="#fff" stroke-width="1.1"><rect x="1" y="2.5" width="11" height="10"/><path d="M1 5.5h11M4 1v3M9 1v3"/><circle cx="10.5" cy="10.5" r="2.3" fill="var(--teal)"/></svg>CALENDAR</li>
      <li><svg viewBox="0 0 14 14" fill="none" stroke="#fff" stroke-width="1.1"><circle cx="7" cy="7" r="6"/><circle cx="7" cy="7" r="3.8"/><circle cx="7" cy="7" r="1.6"/></svg>EXPENSES</li>
      <li><svg viewBox="0 0 14 14" fill="none" stroke="#fff" stroke-width="1.1"><path d="M1 13h12M2 13V9h2v4M6 13V7h2v6M10 13V5h2v8M2 6l4-3 3 2 4-4"/></svg>PERFORMANCE</li>
      <li><svg viewBox="0 0 14 14" fill="none" stroke="#fff" stroke-width="1.1"><rect x="2" y="1" width="8" height="12"/><path d="M4 4h4M4 6.5h4M4 9h4M10 5h2v8h-2"/></svg>REPORTS</li>
      <li><svg viewBox="0 0 10 10"><use href="#ico-gear"/></svg>SETTINGS</li>
      <li></li>
      <li></li>
    </ul>
  </aside>
  <header class="topbar">
    <div class="user"><span class="avatar" role="img" aria-label="User avatar"></span><span>ADMIN, DEMO<br>HR ADMINISTRATOR</span><svg class="chev" viewBox="0 0 8 8"><path d="M1 3l3 3 3-3" fill="none" stroke="#333" stroke-width="1"/></svg></div>
  </header>
  <table class="orders">
    <colgroup><col style="width:54px"><col style="width:111px"><col style="width:134px"><col style="width:170px"><col style="width:61px"><col style="width:174px"><col style="width:71px"><col style="width:60px"><col style="width:40px"></colgroup>
    <thead><tr><th>ORDER</th><th>ORIGIN</th><th>DESTINATION</th><th>CUSTOMER</th><th>STATUS</th><th class="center">TONS</th><th class="center">WAIT TIME</th><th class="center">REMAINING</th><th>+/-<svg class="hd-truck"><use href="#ico-truck-grey"/></svg></th></tr></thead>
    <tbody>
      <tr><td>17746</td><td>Marlow Asphalet Plant</td><td>KRTM - 185 from mm 77-98</td><td>Hollis Construction = North Division</td><td>Accepted</td><td class="tons"><div class="bar"><i style="width:53%"></i></div><div class="tons-meta"><span>722.57/1500</span><span>7.30am-5.00pm</span></div></td><td class="wait"><svg><use href="#ico-wait"/></svg></td><td class="rem up">+1.25 hrs</td><td class="diff down">-31</td></tr>
      <tr><td>17747</td><td>Carver Asphalet Plant</td><td>Maple Sprins</td><td>Hollis Construction = North Division</td><td>Accepted</td><td class="tons"><div class="bar"><i style="width:100%"></i></div><div class="tons-meta"><span>1830.79 / 1000</span><span>7.30am-5.00pm</span></div></td><td class="wait"><svg><use href="#ico-wait"/></svg></td><td class="rem down">-0.28 hrs</td><td class="diff up">+16</td></tr>
      <tr><td>17794</td><td>Marlow Asphalet Plant</td><td>KRTM - 185 from mm 77-98</td><td>Hollis Construction = North Division</td><td>Accepted</td><td class="tons"><div class="bar"></div><div class="tons-meta"><span>0.00 / 100</span><span>8.00pm - 4.00am</span></div></td><td class="wait"><svg><use href="#ico-wait"/></svg></td><td class="rem">8.00 hrs</td><td class="diff up">-</td></tr>
      <tr><td>17746</td><td>Marlow Asphalet Plant</td><td>KRTM - 185 from mm 77-98</td><td>Hollis Construction = North Division</td><td>Accepted</td><td class="tons"><div class="bar"><i style="width:53%"></i></div><div class="tons-meta"><span>722.57/1500</span><span>7.30am-5.00pm</span></div></td><td class="wait"><svg><use href="#ico-wait"/></svg></td><td class="rem up">+1.25 hrs</td><td class="diff down">-31</td></tr>
      <tr><td>17747</td><td>Carver Asphalet Plant</td><td>Maple Sprins</td><td>Hollis Construction = North Division</td><td>Accepted</td><td class="tons"><div class="bar"><i style="width:100%"></i></div><div class="tons-meta"><span>1830.79 / 1000</span><span>7.30am-5.00pm</span></div></td><td class="wait"><svg><use href="#ico-wait"/></svg></td><td class="rem down">-0.28 hrs</td><td class="diff up">+16</td></tr>
      <tr><td>17794</td><td>Marlow Asphalet Plant</td><td>KRTM - 185 from mm 77-98</td><td>Hollis Construction = North Division</td><td>Accepted</td><td class="tons"><div class="bar"></div><div class="tons-meta"><span>0.00 / 100</span><span>8.00pm - 4.00am</span></div></td><td class="wait"><svg><use href="#ico-wait"/></svg></td><td class="rem">8.00 hrs</td><td class="diff up">-</td></tr>
    </tbody>
  </table>

  <div class="cycle">
    <div class="cycle-title">Avg Cycle Time : 2hr 27mins</div>
    <div class="leg"><span class="leg-icon"><svg><use href="#ico-plant"/></svg></span><div class="leg-body"><div class="leg-name">Plat (min)</div><div class="leg-row"><span>Planned : 30</span><span>Actual : 33</span></div></div></div>
    <div class="leg"><span class="leg-icon"><svg><use href="#ico-truck"/></svg></span><div class="leg-body"><div class="leg-name">Driving (min)</div><div class="leg-row"><span>Planned : 30</span><span>Actual : 33</span></div></div></div>
    <div class="leg"><span class="leg-icon"><svg><use href="#ico-pin"/></svg></span><div class="leg-body"><div class="leg-name">Jobsite (min)</div><div class="leg-row"><span>Planned : 30</span><span>Actual : 33</span></div></div></div>
    <div class="leg"><span class="leg-icon"><svg><use href="#ico-gear"/></svg></span><div class="leg-body"><div class="leg-name">Equipment (min)</div><div class="leg-row"><span>Planned : 30</span><span>Actual : 33</span></div></div></div>
  </div>

  <nav class="pager"><span class="arrow">‹</span><span class="on">1</span><span>2</span><span>3</span><span>4</span><span>5</span><span class="arrow">›</span></nav>
  <p class="copyright">Copyright © 2020 All Rights Reserved</p>
  <p class="code">X37</p>
</section>

</body>
</html>
```